Design a fresh new presentation folder for us!

We are looking for a fresh design of our new presentation folder.<br/><br/>We would like our current logo and colours being used in the design as well as images associated with our industry being international logistics.<br/><br/>Our services include, international freight - sea and air, domestic road transport, 3pl and warehousing.<br/><br/>We will attach our logo and other images we have used in the past to give you an idea of what we are after. Also attached our old folder.<br/><br/>We want a brand new fresh approach that is a really modern design. It needs to be visually striking.

Industry/Entity Type

Logistic

Colors
9ccb3b
acd037
cadf82
eef4d8

Requirements
Must have
• Fresh. Modern. Visually striking. Industry related.
• Slogan - Local Knowledge, Global Strength or Complete Logistics Solutions

```html
<!DOCTYPE html>
<html lang="en">
<head>
<meta charset="utf-8">
<title>Northway Freight – Presentation Folder</title>
<link rel="stylesheet" href="https://fonts.googleapis.com/css2?family=Cinzel:wght@600;700&family=Montserrat:wght@700&family=Open+Sans:wght@400;600&display=swap">
<style>
  :root {
    --brand-green: #9ccb3b;
    --brand-lime: #acd037;
    --brand-pale: #cadf82;
    --brand-mist: #eef4d8;
    --ink: #000000;
    --paper: #ffffff;
    --slate: #7d7d7d;
    --slate-light: #a4a4a4;
    --stage: #e4e4e4;
  }
  html, body {
    margin: 0;
    padding: 0;
    width: 1000px;
    height: 1200px;
    overflow: hidden;
    background: var(--stage);
  }
  .folder-sheet { display: block; width: 1000px; height: 1200px; }
  .brand-name { font-family: "Montserrat", sans-serif; font-weight: 700; fill: var(--brand-green); letter-spacing: 0.5px; }
  .office-title { font-family: "Cinzel", serif; font-weight: 600; fill: var(--brand-green); font-size: 13px; }
  .office-detail { font-family: "Open Sans", sans-serif; font-weight: 400; fill: var(--paper); font-size: 7.5px; }
  .office-web { font-family: "Open Sans", sans-serif; font-weight: 600; fill: var(--paper); font-size: 9px; }
  .slogan { font-family: "Cinzel", serif; font-weight: 700; font-size: 19px; }
  .slogan-green { fill: var(--brand-green); }
  .slogan-white { fill: var(--paper); }
  .site-band-text { font-family: "Cinzel", serif; font-weight: 600; fill: var(--paper); font-size: 10px; letter-spacing: 1px; }
  .card-slot-text { font-family: "Open Sans", sans-serif; font-weight: 400; fill: var(--paper); font-size: 13px; }
  .call-line { font-family: "Cinzel", serif; font-weight: 700; fill: var(--ink); font-size: 16px; }
</style>
</head>
<body>
<svg class="folder-sheet" viewBox="0 0 1000 1200" xmlns="http://www.w3.org/2000/svg">
  <defs>
    <linearGradient id="harbour-tones" x1="0" y1="0" x2="1" y2="1">
      <stop offset="0" stop-color="#3f6aa8"/>
      <stop offset="0.45" stop-color="#5c8fc4"/>
      <stop offset="0.7" stop-color="#b0683a"/>
      <stop offset="1" stop-color="#9a1e1e"/>
    </linearGradient>
    <linearGradient id="sky-tones" x1="0" y1="0" x2="0" y2="1">
      <stop offset="0" stop-color="#4a5a78"/>
      <stop offset="0.35" stop-color="#d58a4c"/>
      <stop offset="0.6" stop-color="#f3c58e"/>
      <stop offset="1" stop-color="#2f3440"/>
    </linearGradient>
    <linearGradient id="road-tones" x1="0" y1="0" x2="1" y2="1">
      <stop offset="0" stop-color="#6c6c6c"/>
      <stop offset="0.55" stop-color="#c9c9c9"/>
      <stop offset="1" stop-color="#8e8e8e"/>
    </linearGradient>
    <linearGradient id="site-band" x1="0" y1="0" x2="0" y2="1">
      <stop offset="0" stop-color="var(--slate-light)"/>
      <stop offset="1" stop-color="var(--slate)"/>
    </linearGradient>
  </defs>

  <!-- Outside spread -->
  <g class="outside-spread" transform="translate(140 40)">
    <g class="back-cover">
      <rect width="360" height="500" fill="var(--ink)"/>
      <polygon class="back-photo" points="0,0 360,0 360,40 195,310 0,380" fill="url(#harbour-tones)" role="img" aria-label="Photo of a container ship loaded at a port with cranes"/>
      <polygon class="back-photo-edge" points="360,95 360,270 240,298" fill="#3d5f93" role="img" aria-label="Continuation of the port photo"/>
      <polygon class="back-green-stripe" points="360,40 360,95 240,298 195,310" fill="var(--brand-green)"/>
      <polygon class="back-green-corner" points="0,380 195,310 100,500 0,500" fill="var(--brand-lime)"/>
      <g class="office-block" transform="translate(215 0)">
        <text class="brand-name" x="0" y="338" font-size="10">NORTHWAY FREIGHT</text>
        <text class="office-title" x="0" y="372">Head Office</text>
        <text class="office-detail" x="0" y="386">48 Harbour Lane, Kestrel Park,</text>
        <text class="office-detail" x="0" y="396">NSW 2100, Australia</text>
        <text class="office-detail" x="0" y="414">Tel: +61 2 5550 0142</text>
        <text class="office-detail" x="0" y="424">Fax: +61 2 5550 0178</text>
        <text class="office-web" x="0" y="442">www.northwayfreight.com</text>
      </g>
    </g>
    <g class="front-cover" transform="translate(360 0)">
      <rect width="360" height="500" fill="var(--ink)"/>
      <rect class="front-photo" width="360" height="300" fill="url(#sky-tones)" role="img" aria-label="Photo of a passenger jet on a runway with a container port behind at sunset"/>
      <polygon points="0,0 25,0 0,45" fill="#3a5583"/>
      <polygon class="front-green-stripe" points="25,0 60,0 0,105 0,45" fill="var(--brand-green)"/>
      <text class="brand-name" x="30" y="342" font-size="17">NORTHWAY FREIGHT</text>
      <text class="slogan slogan-green" x="30" y="386">Local Knowledge, Global</text>
      <text class="slogan slogan-green" x="30" y="410">Strength or Complete</text>
      <text class="slogan slogan-white" x="30" y="434">Logistics Solutions</text>
      <rect class="site-band" y="456" width="360" height="44" fill="url(#site-band)"/>
      <text class="site-band-text" x="180" y="482" text-anchor="middle">WWW.NORTHWAYFREIGHT.COM</text>
    </g>
  </g>

  <!-- Inside spread -->
  <g class="inside-spread" transform="translate(140 640)">
    <g class="inside-left">
      <rect width="360" height="500" fill="var(--paper)"/>
      <text class="brand-name" x="180" y="200" font-size="24" text-anchor="middle">NORTHWAY FREIGHT</text>
      <path class="left-pocket" d="M0,370 L340,330 Q358,328 362,345 L360,500 L0,500 Z" fill="var(--ink)"/>
      <polygon class="card-slot" points="108,402 212,392 226,404 230,468 216,480 112,488 100,476 96,414" fill="var(--slate)"/>
      <text class="card-slot-text" x="163" y="434" text-anchor="middle">Space for</text>
      <text class="card-slot-text" x="163" y="452" text-anchor="middle">Business card</text>
    </g>
    <g class="inside-right" transform="translate(360 0)">
      <rect class="inside-photo" width="360" height="500" fill="url(#road-tones)" role="img" aria-label="Black and white photo of a delivery truck on a road"/>
      <path class="right-pocket" d="M0,500 L0,330 Q0,314 18,312 L320,300 L360,500 Z" fill="var(--brand-green)"/>
      <text class="call-line" x="175" y="420" text-anchor="middle">Call 1300 555 017</text>
    </g>
  </g>
</svg>
</body>
</html>
```